Onlineshop VORMA braucht ein Design!
Zielgruppe
Wir entwickeln innovative Produkte. Für dieses Projekt haben wir 2 Zielgruppen: Kinder und Erwachsene.
Hallo,
wir haben ein neuartiges Tragesystem entwickelt, das dem Träger der Tasche das Tragen erleichtert. Im Moment arbeiten wir daran, dieses System für eine eigene Schultaschenlinie zu verwenden. Später wollen wir unsere Produktpalette erweitern und ebenso Zubehör hierzu(z.B. Regenschirm, Mütze etc.) mit anbieten. Als weiterer Schritt sind zudem auch andere Taschen (z.B. Rucksäcke) für Erwachsene geplant.
Unser Produkt ist einmalig und genau deshalb möchten wir eine Homepage mit Shopware 4 Community Edition eine prägnanten und übersichtlichen Shop, sowie ein Blog erstellen.
Das Logo für unser Schultaschenprojekt befindet sich im Anhang und kann farblich angepasst werden. Wir benötigen einen kindergerechten, gleichzeitig seriösen Internetauftritt und es kann auch gerne ein komplettes Template erstellt werden für Shopware 4 oder ein Design-Vorschlag (Photoshop) eingebracht werden.
Wir bitten euch die Photoshop-Design Vorlagen ohne verbundene Ebenen und Pfade anzulegen. Bei Templates, bitten wir um eine genauere detaillierte Information zum Aufbau, Struktur etc..

```html
<!DOCTYPE html>
<html lang="de">
<head>
<meta charset="utf-8">
<title>VORMA – Onlineshop</title>
<link href="https://fonts.googleapis.com/css2?family=Open+Sans:wght@400;600&family=Oswald:wght@400;500&family=Ubuntu:wght@300;400;500&display=swap" rel="stylesheet">
<style>
  :root{
    --orange:#e35d1c;
    --ink:#1b1b1b;
    --muted:#8c8c8c;
    --panel:#e1e1e1;
    --footer:#262626;
    --white:#ffffff;
    --soft:#f5f5f5;
  }
  *{box-sizing:border-box;margin:0;padding:0}
  html,body{width:739px;height:1200px;overflow:hidden;background:var(--white)}
  body{position:relative;font-family:"Ubuntu",sans-serif;color:var(--ink)}
  .abs{position:absolute}

  .main-nav{left:88px;top:16px;width:562px;height:21px;background:var(--orange)}
  .main-nav a{position:absolute;top:4px;color:var(--white);font:400 10.5px "Open Sans",sans-serif;text-decoration:none;letter-spacing:.2px}

  .brand-rule{left:88px;top:46px;width:3px;height:53px;background:var(--orange)}
  .brand{left:110px;top:56px;font:500 26px "Ubuntu",sans-serif;color:var(--orange);letter-spacing:1px}

  .cart{left:564px;top:68px;width:85px;height:31px;border-bottom:3px solid var(--orange)}
  .cart svg{position:absolute;left:8px;top:6px}
  .cart-count{position:absolute;left:45px;top:0;font:400 11px "Oswald",sans-serif;color:var(--orange)}
  .cart-sum{position:absolute;left:45px;top:14px;font:400 10px "Oswald",sans-serif;color:var(--ink)}

  .hero{left:116px;top:135px;width:509px;height:255px;background:var(--white);border:1px solid #ececec;box-shadow:0 6px 6px -4px rgba(0,0,0,.25)}
  .hero-photo{position:absolute;left:41px;top:16px;width:221px;height:232px;background:radial-gradient(ellipse at 50% 45%,#c9d43a 0%,#8f8f5a 45%,#f6f6f6 75%)}
  .hero-kicker{position:absolute;left:240px;top:92px;font:300 19px "Ubuntu",sans-serif;color:var(--muted)}
  .hero-claim{position:absolute;left:240px;top:120px;font:400 32px "Ubuntu",sans-serif;color:var(--orange)}

  .slider-dot{top:416px;width:38px;height:2px;background:#a8a8a8}
  .slider-dot.is-active{background:var(--orange)}

  .product{top:493px;width:171px;height:183px;background:var(--white);border-top:5px solid var(--orange);box-shadow:0 1px 5px rgba(0,0,0,.3)}
  .product-photo{position:absolute;left:11px;top:17px;width:100px;height:148px}
  .product-name{position:absolute;right:12px;top:26px;font:500 13px "Oswald",sans-serif;color:var(--ink);letter-spacing:-.2px}
  .product-price{position:absolute;right:14px;top:40px;font:400 23px "Ubuntu",sans-serif;color:var(--orange);letter-spacing:-1px}
  .product-price sup{font-size:9px;color:var(--ink);vertical-align:10px;letter-spacing:0}
  .product-tab{position:absolute;right:-6px;top:22px;width:9px;height:36px;background:var(--orange)}
  .product-more{position:absolute;right:13px;top:139px;font:400 10.5px "Ubuntu",sans-serif;color:var(--muted);text-decoration:underline}

  .discount{left:95px;top:676px;width:42px;height:40px;background:var(--orange);color:var(--white);text-align:center;padding-top:6px}
  .discount b{display:block;font:500 12px "Oswald",sans-serif;line-height:13px}
  .discount span{display:block;font:500 6px "Oswald",sans-serif;line-height:10px}

  .about{left:88px;top:747px;width:562px;height:270px;background:var(--panel)}
  .about-brand{position:absolute;left:13px;top:20px;font:500 14px "Ubuntu",sans-serif;color:#555;letter-spacing:1px}
  .about-title{position:absolute;left:13px;top:40px;font:400 22px "Ubuntu",sans-serif;color:var(--orange)}
  .about-text{position:absolute;left:15px;top:78px;width:255px;font:300 10.4px/13.9px "Ubuntu",sans-serif;color:#333}
  .about-video-label{position:absolute;right:17px;top:31px;font:400 11px "Ubuntu",sans-serif;color:var(--orange)}
  .video{position:absolute;left:308px;top:61px;width:240px;height:148px;background:var(--soft);border:1px solid #d8d8d8;border-radius:5px;box-shadow:0 6px 5px -5px rgba(0,0,0,.3)}
  .video svg{position:absolute;left:80px;top:39px}

  .site-footer{left:88px;top:1017px;width:563px;height:123px;background:var(--footer)}
  .footer-col{position:absolute;top:8px}
  .footer-col h3{font:400 11px "Ubuntu",sans-serif;color:var(--orange);margin-bottom:3px}
  .footer-col a{display:block;font:400 7.5px/15.4px "Open Sans",sans-serif;color:var(--white);text-decoration:none}
  .footer-brand{position:absolute;right:11px;top:36px;font:500 14px "Ubuntu",sans-serif;color:#cfcfcf;letter-spacing:1px}
  .footer-note{position:absolute;right:11px;top:56px;font:400 7.5px "Open Sans",sans-serif;color:var(--white)}
  .footer-social{position:absolute;right:11px;top:73px;display:flex;gap:5px}
  .footer-social i{display:block;width:12px;height:12px;border-radius:50%;background:#9a9a9a}
  .footer-accent{position:absolute;left:175px;bottom:0;width:212px;height:8px;background:var(--orange)}
</style>
</head>
<body>

<nav class="abs main-nav">
  <a style="left:22px">HOME</a>
  <a style="left:90px">IMPRESSUM</a>
  <a style="left:183px">KONTAKT</a>
  <a style="left:252px">ÜBER UNS</a>
</nav>

<div class="abs brand-rule"></div>
<div class="abs brand">VORMA</div>

<div class="abs cart">
  <svg width="28" height="20" viewBox="0 0 28 20" aria-hidden="true">
    <path d="M1 2h4l3 11h15l3-8H7" fill="none" stroke="#333" stroke-width="2"/>
    <path d="M9 8h15M10 11h12" stroke="#333" stroke-width="1.2"/>
    <circle cx="10" cy="17" r="2" fill="#333"/><circle cx="21" cy="17" r="2" fill="#333"/>
  </svg>
  <span class="cart-count">0 Artikel</span>
  <span class="cart-sum">0,00 €</span>
</div>

<section class="abs hero">
  <div class="hero-photo" role="img" aria-label="Foto eines gelb-grauen Trekkingrucksacks"></div>
  <p class="hero-kicker">unsere Rucksäcke</p>
  <p class="hero-claim">haben Rückgrat!</p>
</section>

<div class="abs slider-dot" style="left:308px"></div>
<div class="abs slider-dot is-active" style="left:353px"></div>
<div class="abs slider-dot" style="left:397px"></div>

<article class="abs product" style="left:88px">
  <div class="product-photo" role="img" aria-label="Foto eines rot-grauen Trekkingrucksacks" style="background:linear-gradient(180deg,#d8322e 0%,#c9c9c9 35%,#bdbdbd 70%,#2a2a2a 100%)"></div>
  <h2 class="product-name">RUCKSACK 1</h2>
  <p class="product-price">55,59<sup>€</sup></p>
  <div class="product-tab"></div>
  <a class="product-more">weiter</a>
</article>

<article class="abs product" style="left:285px">
  <div class="product-photo" role="img" aria-label="Foto eines schwarz-grauen Laptoprucksacks" style="background:linear-gradient(180deg,#f2f2f2 0%,#3a3a3a 30%,#9a9a9a 60%,#1e1e1e 100%)"></div>
  <h2 class="product-name">RUCKSACK 1</h2>
  <p class="product-price">55,59<sup>€</sup></p>
  <div class="product-tab"></div>
  <a class="product-more">weiter</a>
</article>

<article class="abs product" style="left:480px">
  <div class="product-photo" role="img" aria-label="Foto eines dunkelblauen Schulrucksacks" style="background:linear-gradient(180deg,#f6f6f6 0%,#3c4a66 30%,#2b3750 75%,#f4f4f4 100%)"></div>
  <h2 class="product-name">RUCKSACK 1</h2>
  <p class="product-price">55,59<sup>€</sup></p>
  <div class="product-tab"></div>
  <a class="product-more">weiter</a>
</article>

<div class="abs discount"><b>30%</b><span>RABATT</span></div>

<section class="abs about">
  <div class="about-brand">VORMA</div>
  <h2 class="about-title">Wer sind wir?</h2>
  <p class="about-text">Lorem ipsum dolor sit amet, consetetur sadipscing elitr, sed diam nonumy eirmod tempor invidunt ut labore et dolore magna aliquyam erat, sed diam voluptua. At vero eos et accusam et justo duo dolores et ea rebum. Stet clita kasd gubergren, no sea takimata sanctus est Lorem ipsum dolor sit amet. Lorem ipsum dolor sit amet, consetetur sadipscing elitr, sed diam nonumy eirmod tempor invidunt ut labore et dolore magna aliquyam erat.</p>
  <span class="about-video-label">Video</span>
  <div class="video">
    <svg width="70" height="70" viewBox="0 0 70 70" aria-label="Video abspielen">
      <circle cx="35" cy="35" r="35" fill="#e35d1c"/>
      <path d="M31 28l9 7-9 7z" fill="#fff"/>
    </svg>
  </div>
</section>

<footer class="abs site-footer">
  <div class="footer-col" style="left:16px">
    <h3>Footer 1</h3>
    <a>HOME</a><a>IMPRESSUM</a><a>KONTAKT</a><a>MENU2</a><a>MENU3</a>
  </div>
  <div class="footer-col" style="left:130px">
    <h3>Footer 2</h3>
    <a>HOME</a><a>IMPRESSUM</a><a>KONTAKT</a><a>MENU2</a><a>MENU3</a>
  </div>
  <div class="footer-col" style="left:245px">
    <h3>Footer 3</h3>
    <a>HOME</a><a>IMPRESSUM</a><a>KONTAKT</a><a>MENU2</a><a>MENU3</a>
  </div>
  <div class="footer-brand">VORMA</div>
  <p class="footer-note">Sie finden uns auch auf</p>
  <div class="footer-social"><i></i><i></i><i></i><i></i></div>
  <div class="footer-accent"></div>
</footer>

</body>
</html>
```